New Innovative Counselling and psychotherapy Service needs Business Card design

Keep it simple and professional. On one side, just company name and logo (perhaps in all blue) and maybe a tag line.

On other side (all white) my name and Qualifications in centre

Industry/Entity Type

Health And Wellness

Contact Information for Business Card

Derek Hollis
Counsellor & Psychotherapist
BSc (Psychol.), BA, Dip. (Couns. & Psych.), PG.Cert (CBT), MGVrA, NWTF

I will also require Mobile no, Email and web site address of which I'll pass on to final designer.

Font styles to use
Sans Serif

Requirements
Must have
• My Logo Only and please use the colours in logo that is in it.
Should not have
• Any other images

```html
<!DOCTYPE html>
<html lang="en">
<head>
<meta charset="utf-8">
<title>Kindred Lane – Business Card</title>
<link rel="stylesheet" href="https://fonts.googleapis.com/css2?family=Montserrat:wght@300;400;500;700&display=swap">
<style>
  :root {
    --sky: #4ba6d6;
    --sky-soft: #cfe3ee;
    --leaf: #8db65d;
    --leaf-soft: #e3ead9;
    --ink: #4a4a4a;
    --ink-soft: #5c5c5c;
    --paper: #ffffff;
    --paper-tint: #f6f6f6;
    --backdrop: #ececec;
  }
  * { margin: 0; padding: 0; box-sizing: border-box; }
  html, body {
    width: 1200px; height: 1188px; overflow: hidden;
    background: var(--backdrop);
    font-family: "Montserrat", sans-serif;
  }
  .sheet {
    width: 1200px; height: 1188px;
    display: flex; flex-direction: column;
    align-items: center; justify-content: space-evenly;
  }
  .card {
    position: relative; overflow: hidden;
    width: 840px; height: 480px;
    box-shadow: 0 6px 24px rgba(0,0,0,0.08);
  }
  .card-decor { position: absolute; inset: 0; width: 100%; height: 100%; }

  /* Front: details side */
  .card--details { background: linear-gradient(160deg, var(--paper), var(--paper-tint)); }
  .brand { position: absolute; display: flex; align-items: center; gap: 18px; }
  .brand-dot { border-radius: 50%; background: var(--sky); flex: none; }
  .brand-name { font-weight: 300; white-space: nowrap; }
  .card--details .brand { left: 64px; top: 60px; }
  .card--details .brand-dot { width: 54px; height: 54px; }
  .card--details .brand-name { font-size: 40px; color: var(--ink); letter-spacing: 0.5px; }

  .person { position: absolute; left: 64px; top: 150px; color: var(--ink); }
  .person-name { font-size: 38px; font-weight: 700; letter-spacing: 0.5px; }
  .person-role { font-size: 19px; font-weight: 400; margin-top: 6px; }
  .person-quals { font-size: 18px; font-weight: 400; line-height: 1.45; margin-top: 4px; color: var(--ink-soft); }

  .contact { position: absolute; left: 64px; top: 342px; list-style: none; color: var(--ink); font-size: 18px; }
  .contact li { display: flex; align-items: center; gap: 14px; line-height: 32px; }
  .contact svg { width: 20px; height: 20px; flex: none; }

  /* Back: brand side */
  .card--brand { background: var(--sky); }
  .card--brand .brand { left: 150px; top: 150px; }
  .card--brand .brand-dot { width: 84px; height: 84px; background: var(--paper); }
  .card--brand .brand-name { font-size: 66px; color: var(--paper); letter-spacing: 1px; }
  .brand-web {
    position: absolute; left: 150px; top: 290px;
    color: var(--paper); font-size: 20px; font-weight: 400; letter-spacing: 3px;
  }
</style>
</head>
<body>
<main class="sheet">

  <section class="card card--details" aria-label="Business card, details side">
    <svg class="card-decor" viewBox="0 0 840 480" aria-hidden="true">
      <circle cx="700" cy="390" r="210" fill="var(--sky-soft)" opacity="0.55"/>
    </svg>
    <div class="brand">
      <span class="brand-dot"></span>
      <span class="brand-name">Kindred Lane</span>
    </div>
    <div class="person">
      <h1 class="person-name">Derek Hollis</h1>
      <p class="person-role">Counsellor &amp; Psychotherapist</p>
      <p class="person-quals">BSc (Psychol.)<br>BA, Dip. (Couns. &amp; Psych.)<br>PG.Cert (CBT), MGVrA, NWTF</p>
    </div>
    <ul class="contact">
      <li>
        <svg viewBox="0 0 24 24" aria-hidden="true"><path d="M6.6 10.8a15 15 0 0 0 6.6 6.6l2.2-2.2a1 1 0 0 1 1-.25 11.4 11.4 0 0 0 3.6.57 1 1 0 0 1 1 1V20a1 1 0 0 1-1 1A17 17 0 0 1 3 4a1 1 0 0 1 1-1h3.5a1 1 0 0 1 1 1c0 1.25.2 2.45.57 3.57a1 1 0 0 1-.25 1z" fill="var(--sky)"/></svg>
        <span>000 000 0000</span>
      </li>
      <li>
        <svg viewBox="0 0 24 24" aria-hidden="true"><rect x="2.5" y="5" width="19" height="14" rx="1.5" fill="none" stroke="var(--sky)" stroke-width="1.8"/><path d="M3 6l9 7 9-7" fill="none" stroke="var(--sky)" stroke-width="1.8"/></svg>
        <span>derek@kindredlane.com</span>
      </li>
      <li>
        <svg viewBox="0 0 24 24" aria-hidden="true"><g fill="none" stroke="var(--sky)" stroke-width="1.6"><circle cx="12" cy="12" r="9"/><ellipse cx="12" cy="12" rx="4" ry="9"/><path d="M3 12h18M4.5 7.5h15M4.5 16.5h15"/></g></svg>
        <span>www.kindredlane.com</span>
      </li>
    </ul>
  </section>

  <section class="card card--brand" aria-label="Business card, brand side">
    <svg class="card-decor" viewBox="0 0 840 480" aria-hidden="true">
      <circle cx="680" cy="400" r="200" fill="var(--paper)" opacity="0.1"/>
    </svg>
    <div class="brand">
      <span class="brand-dot"></span>
      <span class="brand-name">Kindred Lane</span>
    </div>
    <p class="brand-web">www.kindredlane.com</p>
  </section>

</main>
</body>
</html>
```